Design a website for a newly developed Delta 8 THC Company

Design a responsive Website with the following goals in mind:
- Built on Wordpress/WooCommerce theme. Please use this when designing for ease of integration.
- Build trust with website visitors with an engaging, informative content driven website, that leads to a conversion of product purchase and repeat business. We will also be driving consumers to businesses that carry our products as well.
- The website will embody a lifestyle feel and make the visitor identify with the content.
- The website will allow for super charged SEO and other digital marketing and advertising strategies and tactics used to increase discovery, awareness, and conversion.
Please see additional goals in the uploaded files.
Target Market(s)
Male/Female 21-
Industry/Entity Type
Cannabis/Hemp
Coding
Coded - Design and coding required
Number of Pages Required
5+ page
Font styles to use
Other font styles liked:
- Montserrat
Look and feel
Each slider illustrates characteristics of the customer's brand and the style your logo design should communicate.

```html
<!DOCTYPE html>
<html lang="en">
<head>
<meta charset="utf-8">
<title>Lumera Delta 8 Gummies – Sour Apple</title>
<link rel="stylesheet" href="https://fonts.googleapis.com/css2?family=Poppins:wght@400;500;600;700&family=Playfair+Display:wght@700;800&display=swap">
<style>
:root{
  --gold-1:#f3e36a;
  --gold-2:#d9b94d;
  --gold-3:#c09531;
  --gold-text:#b88a24;
  --apple:#8dbb3f;
  --ink:#1f1f1f;
  --body:#555;
  --muted:#777;
  --line:#e6e6e6;
  --soft:#f7f7f7;
  --footer:#3b3b3c;
  --white:#fff;
}
*{box-sizing:border-box;margin:0;padding:0}
html,body{width:730px;height:1200px;overflow:hidden}
body{position:relative;background:var(--white);font-family:"Poppins",sans-serif;color:var(--ink)}
.abs{position:absolute}
.gold-grad{background:linear-gradient(90deg,var(--gold-1),var(--gold-3))}

.top-bar{left:0;top:0;width:730px;height:19px;background:linear-gradient(90deg,#efe08a,#c7992f);font-size:7px;font-weight:500;text-align:center;line-height:19px;color:#3a3220}

.brand{left:95px;top:30px;width:44px;text-align:center}
.brand-mark{width:22px;height:22px;border-radius:50%;border:1.5px solid var(--ink);margin:0 auto 4px}
.brand-name{font-size:7px;font-weight:500;letter-spacing:2px}

.main-nav{font-size:7px;font-weight:500;color:var(--ink)}
.main-nav a{color:inherit;text-decoration:none;position:absolute;white-space:nowrap}
.nav-icons{top:33px;left:600px}

.gallery{left:95px;top:108px;width:212px;height:282px;border:1px solid #eee}
.gallery-main{left:44px;top:20px;width:124px;height:174px;border-radius:4px;background:linear-gradient(160deg,#4a4a46,#222220)}
.gallery-arrow{width:14px;height:14px;border-radius:50%;background:#fff;box-shadow:0 1px 4px rgba(0,0,0,.15);display:flex;align-items:center;justify-content:center;top:100px}
.gallery-divider{left:0;top:219px;width:210px;height:1px;background:#eee}
.thumb{top:227px;width:58px;height:46px;background:#f5f5f5;display:flex;align-items:center;justify-content:center}
.thumb span{display:block;width:42px;height:46px;background:linear-gradient(160deg,#4a4a46,#222220)}
.thumb.active{border:1px solid var(--apple);background:#fff}
.thumb.active span{width:26px;height:38px}

.product-title{left:353px;top:94px;font-size:17.5px;font-weight:400;white-space:nowrap}
.flavour{font-family:"Playfair Display",serif;font-weight:800;color:var(--apple);letter-spacing:.5px;white-space:nowrap}
.flavour.lg{left:352px;top:117px;font-size:26px}
.rating{left:353px;top:159px;display:flex;align-items:center;gap:1px;font-size:5.5px;color:#333}
.rating .sep{width:1px;height:8px;background:#ddd;margin:0 13px}
.description{left:354px;top:178px;width:282px;font-size:8px;line-height:13.7px;color:var(--body)}
.btn{border-radius:12px;font-size:6.3px;font-weight:700;color:#2c2512;display:flex;align-items:center;justify-content:center;gap:5px;letter-spacing:.2px;white-space:nowrap}
.wishlist{left:352px;top:259px;width:97px;height:23px}

.cart-box{left:353px;top:305px;width:283px;height:107px;background:var(--soft);border:1px solid #e8e8e8}
.cart-name{left:17px;top:17px;font-size:8.2px;white-space:nowrap}
.flavour.sm{left:17px;top:32px;font-size:10px}
.price{left:19px;top:53px;font-size:15px;font-weight:700;color:var(--gold-text)}
.stock{left:19px;top:73px;font-size:5px;color:var(--gold-text);border:1px solid var(--gold-2);padding:3px 7px}
.qty-label{left:131px;top:20px;font-size:6.5px;color:#333}
.qty{left:130px;top:31px;display:flex;height:16px;border:1px solid #e2e2e2;background:#fff}
.qty span{width:15px;display:flex;align-items:center;justify-content:center;font-size:9px;color:var(--gold-text)}
.qty .val{width:22px;font-size:6px;color:#888;border-left:1px solid #e2e2e2;border-right:1px solid #e2e2e2}
.add-cart{left:190px;top:25px;width:89px;height:23px}

.features{left:353px;top:426px;width:283px;height:31px;border-top:1px solid #eee;border-bottom:1px solid #eee;display:flex}
.feature{flex:1;display:flex;align-items:center;gap:9px;padding-left:8px;font-size:8px;font-weight:600}
.feature+.feature{border-left:1px solid #eee;padding-left:11px}

.tabs{left:0;top:487px;width:730px;height:26px;background:var(--soft);border-top:1px solid #eee;border-bottom:1px solid #eee}
.tab{top:9px;font-size:6px;font-weight:500;color:#333}
.tab.active::after{content:"";position:absolute;left:-1px;right:-2px;top:16px;height:1px;background:var(--gold-2)}

.overview-title{left:122px;top:526px;font-size:14.5px;font-weight:400}
.overview-list{list-style:none;font-size:6.4px;color:#444}
.overview-list li{height:15.1px;position:relative;padding-left:8px;white-space:nowrap}
.overview-list li::before{content:"›";position:absolute;left:0;top:-1px;color:#bbb;font-size:7px}
.overview-text{left:122px;top:638px;width:475px;font-size:6.3px;line-height:11px;color:#555}

.promo{left:0;top:715px;width:730px;height:253px;background:var(--soft)}
.promo-kicker{left:96px;top:67px;font-size:10px;color:var(--gold-text);letter-spacing:.2px;white-space:nowrap}
.promo-title{left:95px;top:79px;font-family:"Playfair Display",serif;font-weight:800;font-size:29px;color:var(--ink);white-space:nowrap}
.promo-text{left:95px;top:123px;width:190px;font-size:8.8px;line-height:12px;color:#555}
.buy-now{left:94px;top:163px;width:79px;height:23px}
.pack-a{left:400px;top:60px;width:110px;height:130px;transform:rotate(-8deg);background:linear-gradient(160deg,#4d4d48,#202020);border-radius:4px}
.pack-b{left:530px;top:42px;width:110px;height:130px;transform:rotate(28deg);background:linear-gradient(160deg,#4d4d48,#202020);border-radius:4px}
.shadow{height:6px;border-radius:50%;background:radial-gradient(ellipse,rgba(0,0,0,.18),transparent 70%)}

.site-footer{left:0;top:977px;width:730px;height:192px;background:var(--footer);color:var(--white)}
.footer-brand{left:95px;top:32px;width:40px;text-align:center}
.footer-brand .brand-mark{border-color:var(--gold-2)}
.footer-brand .brand-name{color:var(--gold-2)}
.footer-about{left:95px;top:87px;width:200px;font-size:6.4px;line-height:11px}
.socials{left:99px;top:135px;display:flex;gap:5px}
.socials span{width:23px;height:23px;border-radius:50%;border:1px solid #5a5a5a;display:flex;align-items:center;justify-content:center}
.socials span::after{content:"";width:4px;height:4px;border-radius:50%;background:var(--gold-2)}
.footer-links{left:476px;top:62px;list-style:none;font-size:7px}
.footer-links li{height:17px}
.footer-contact{left:554px;top:62px;font-size:6px;line-height:9px}
.footer-contact h4{font-size:6.5px;font-weight:600;margin-bottom:11px;white-space:nowrap}
.contact-row{display:flex;gap:5px;margin-bottom:8px;white-space:nowrap}
.contact-row svg{flex:none;margin-top:1px}
.copyright{left:0;top:1169px;width:730px;height:31px;background:var(--soft);font-size:5.5px;color:#666;text-align:center;line-height:31px}
</style>
</head>
<body>

<div class="abs top-bar">Lumera Delta 8 Premium Gummies</div>

<header>
  <div class="abs brand">
    <div class="brand-mark"></div>
    <div class="brand-name">LUMERA</div>
  </div>
  <nav class="abs main-nav" style="left:0;top:35px">
    <a style="left:404px">HOME</a>
    <a style="left:446px">OUR STORY</a>
    <a style="left:505px">SHOP</a>
    <a style="left:545px">CONTACT US</a>
  </nav>
  <svg class="abs nav-icons" width="36" height="14" viewBox="0 0 36 14" aria-label="Search and cart">
    <circle cx="5" cy="5" r="3.6" fill="none" stroke="#1f1f1f" stroke-width="1"/>
    <line x1="7.7" y1="7.7" x2="10.5" y2="10.5" stroke="#1f1f1f" stroke-width="1.1"/>
    <path d="M20 3h2l1.6 6.5h6.5l1.3-4.5h-8.4" fill="none" stroke="#1f1f1f" stroke-width="1"/>
    <circle cx="24.5" cy="11.6" r=".9" fill="#1f1f1f"/><circle cx="29.5" cy="11.6" r=".9" fill="#1f1f1f"/>
    <circle cx="32" cy="2.5" r="2.3" fill="#d9b94d"/>
  </svg>
</header>

<section class="abs gallery">
  <div class="abs gallery-main" role="img" aria-label="Black resealable pouch of Delta-8 sour apple gummies"></div>
  <div class="abs gallery-arrow" style="left:13px"><svg width="6" height="6" viewBox="0 0 6 6"><path d="M5 3H1M3 1L1 3l2 2" fill="none" stroke="#c09531" stroke-width="1"/></svg></div>
  <div class="abs gallery-arrow" style="left:186px"><svg width="6" height="6" viewBox="0 0 6 6"><path d="M1 3h4M3 1l2 2-2 2" fill="none" stroke="#c09531" stroke-width="1"/></svg></div>
  <div class="abs gallery-divider"></div>
  <div class="abs thumb" style="left:11px" role="img" aria-label="Pouch front view"><span></span></div>
  <div class="abs thumb active" style="left:76px" role="img" aria-label="Pouch small view"><span></span></div>
  <div class="abs thumb" style="left:142px" role="img" aria-label="Pouch angled view"><span></span></div>
</section>

<section>
  <h1 class="abs product-title">Lumera Delta 8 Gummies</h1>
  <div class="abs flavour lg">SOUR APPLE</div>
  <div class="abs rating">
    <svg width="52" height="9" viewBox="0 0 52 9" aria-label="5 stars">
      <g fill="#d9b94d">
        <path id="st" d="M4.5 0l1.1 3h3.2L6.2 4.9l1 3.1L4.5 6.2 1.8 8l1-3.1L.2 3h3.2z"/>
        <use href="#st" x="11"/><use href="#st" x="22"/><use href="#st" x="33"/><use href="#st" x="44"/>
      </g>
    </svg>
    <span class="sep"></span><span>1 review(s)</span><span class="sep"></span><span>Add your review</span>
  </div>
  <p class="abs description">Lorem ipsum dolor sit amet, consectetur adipiscing elit, sed do eiusmod amet, consectetu ipsum dolor sit amet, consectetur adipiscing elit, sed do eiusmod it amet, consectetur adipiscing elit, sed do eiusmod amet, consectetu ipsum dolor sit amet, consectetur adipiscing elit, sed do eiusmod</p>
  <a class="abs btn gold-grad wishlist">
    <svg width="9" height="8" viewBox="0 0 9 8"><path d="M4.5 7.3L1 3.8A2 2 0 0 1 4.5 1.3 2 2 0 0 1 8 3.8z" fill="none" stroke="#2c2512" stroke-width="1"/></svg>ADD TO WISHLIST
  </a>

  <div class="abs cart-box">
    <div class="abs cart-name">Lumera Delta 8 Gummies</div>
    <div class="abs flavour sm">SOUR APPLE</div>
    <div class="abs price">$142.80</div>
    <div class="abs stock">In stock.</div>
    <div class="abs qty-label">Quantity</div>
    <div class="abs qty"><span>+</span><span class="val">01</span><span>–</span></div>
    <a class="abs btn gold-grad add-cart">
      <svg width="13" height="11" viewBox="0 0 13 11"><path d="M0 1h2l1.6 6h6.4l1.3-4.2H3" fill="none" stroke="#2c2512" stroke-width="1"/><circle cx="4.5" cy="9.3" r=".9" fill="#2c2512"/><circle cx="9" cy="9.3" r=".9" fill="#2c2512"/></svg>ADD TO CART
    </a>
  </div>

  <div class="abs features">
    <div class="feature">
      <svg width="29" height="14" viewBox="0 0 29 14"><path d="M9 1h14v9H9zM9 4H4L1 7v3h8" fill="none" stroke="#c09531" stroke-width="1"/><circle cx="5" cy="11" r="2" fill="#fff" stroke="#c09531"/><circle cx="19" cy="11" r="2" fill="#fff" stroke="#c09531"/><path d="M24 3h4M25 6h3" stroke="#c09531"/></svg>Free Delivery
    </div>
    <div class="feature">
      <svg width="15" height="15" viewBox="0 0 15 15"><circle cx="7.5" cy="7.5" r="6.8" fill="none" stroke="#c09531"/><path d="M7.5 3.3l1.1 2.6h2.8L9.2 7.6l.9 2.8-2.6-1.6-2.6 1.6.9-2.8-2.2-1.7h2.8z" fill="none" stroke="#c09531" stroke-width=".8"/></svg>Quality Products
    </div>
  </div>
</section>

<nav class="abs tabs">
  <span class="abs tab active" style="left:122px">Overview</span>
  <span class="abs tab" style="left:171px">Reviews</span>
</nav>

<section>
  <h2 class="abs overview-title">Overview</h2>
  <ul class="abs overview-list" style="left:122px;top:555px">
    <li>Dusto odio dignissim qui blandit praesent luptatum zzril</li>
    <li>Avaiusto odio dignissim qui blandit praesent luptatum zzril</li>
    <li>Caiusto odio dignissim qui blandit praesent luptatum zzril</li>
    <li>25mg aiusto odio dignissim qui blandit praesent luptatum zzril</li>
    <li>Husto odio dignissim qui blandit praesent luptatum zzril</li>
  </ul>
  <ul class="abs overview-list" style="left:371px;top:555px">
    <li>Dusto odio dignissim qui blandit praesent luptatum zzril</li>
    <li>Avaiusto odio dignissim qui blandit praesent luptatum zzril</li>
    <li>Caiusto odio dignissim qui blandit praesent luptatum zzril</li>
    <li>25mg aiusto odio dignissim qui blandit praesent luptatum zzril</li>
    <li>Husto odio dignissim qui blandit praesent luptatum zzril</li>
  </ul>
  <p class="abs overview-text">Lorem ipsum dolor sit amet, consectetuer adipiscing elit, sed diam nonummy nibh euismod tincidunt ut laoreet dolore magna aliquam erat volutpat. Ut wisi enim ad minim veniam, quis nostrud exerci tation ullamcorper suscipit lobortis nisl ut aliquip ex ea commodo consequat. Duis autem vel eum iriure dolor in hendrerit in vulputate velit esse molestie consequat, vel illum dolore eu feugiat nulla facilisis at vero eros et accumsan et iusto odio dignissim qui blandit praesent luptatum zzril delenit augue duis dolore te feugait nulla facilisi.</p>
</section>

<section class="abs promo">
  <div class="abs promo-kicker">LUMERA DELTA 8 PREMIUM GUMMIES</div>
  <div class="abs promo-title">100% ORGANIC</div>
  <p class="abs promo-text">Lorem ipsum dolor sit amet, consectetur adipiscing elit, sed do eiusmod</p>
  <a class="abs btn gold-grad buy-now">BUY NOW</a>
  <div class="abs pack-a" role="img" aria-label="Floating pouch of Delta-8 gummies"></div>
  <div class="abs pack-b" role="img" aria-label="Floating pouch of Delta-8 cart vape"></div>
  <div class="abs shadow" style="left:390px;top:217px;width:130px"></div>
  <div class="abs shadow" style="left:525px;top:210px;width:130px"></div>
</section>

<footer>
  <div class="abs site-footer">
    <div class="abs footer-brand">
      <div class="brand-mark" style="width:26px;height:26px"></div>
      <div class="brand-name">LUMERA</div>
    </div>
    <p class="abs footer-about">Sed diam nonummy nibh euismod tincidunt ut laoreet dolore magna aliquam erat volutpat widsi enim ad minim.</p>
    <div class="abs socials" aria-label="Social links"><span></span><span></span><span></span></div>
    <ul class="abs footer-links">
      <li>Home</li><li>Our Story</li><li>Shop</li><li>Contact Us</li>
    </ul>
    <div class="abs footer-contact">
      <h4>Lumera Delta 8 Gummies</h4>
      <div class="contact-row">
        <svg width="7" height="9" viewBox="0 0 7 9"><path d="M3.5 8.5S.5 5.3.5 3.3a3 3 0 0 1 6 0c0 2-3 5.2-3 5.2z" fill="none" stroke="#d9b94d" stroke-width=".8"/><circle cx="3.5" cy="3.3" r="1" fill="none" stroke="#d9b94d" stroke-width=".8"/></svg>
        <span>48 W. Larkin Lane.<br>Suite road 210 Harlow,<br>ST 00000</span>
      </div>
      <div class="contact-row">
        <svg width="7" height="7" viewBox="0 0 7 7"><path d="M1 .5l1.5 1.5-.8 1a4 4 0 0 0 1.8 1.8l1-.8L6 5.5 5 6.5C2.5 6.5.5 4.5.5 1.5z" fill="none" stroke="#d9b94d" stroke-width=".7"/></svg>
        <span>555-014-2283</span>
      </div>
      <div class="contact-row">
        <svg width="7" height="6" viewBox="0 0 7 6"><rect x=".5" y=".5" width="6" height="5" fill="none" stroke="#d9b94d" stroke-width=".7"/><path d="M.5.8l3 2.4 3-2.4" fill="none" stroke="#d9b94d" stroke-width=".7"/></svg>
        <span>info@lumera.com</span>
      </div>
    </div>
  </div>
  <div class="abs copyright">© 2021 Lumera</div>
</footer>

</body>
</html>
```